Health Supplement Series for 60 tablets of pure Gold Petal Grain powder

We need a packaging design theme for a health supplement for international consumers. Our initial product is called 'Gold Petal Grain'. It is for general health and is particularly effective for diabetic symptoms.
We would like to see designs that are clean and fresh.
It should give the impression of professional, premium pharmaceutical grade products.
Our company logo is attached below.

Target Market(s)

International

Industry/Entity Type

Health And Wellness

Font styles to use
Serif
Sans Serif

Requirements
Must have
• Bottle and box packaging required.
• 1st product is bottle of 60 tablets of 0.5gm each.
Should not have
• Seals and other "must buy" "guaranteed" etc

```html
<!DOCTYPE html>
<html lang="en">
<head>
<meta charset="utf-8">
<title>Gold Petal Grain – Supplement Label</title>
<link rel="stylesheet" href="https://fonts.googleapis.com/css2?family=Open+Sans:wght@400;700;800&display=swap">
<style>
  :root {
    --page-bg: #ededed;
    --label-bg: #ffffff;
    --brand-green: #5e9b2c;
    --leaf-light: #a8d46a;
    --leaf-mid: #76b83a;
    --body-text: #3a3a3a;
  }
  html, body {
    margin: 0;
    padding: 0;
    width: 1158px;
    height: 1200px;
    overflow: hidden;
    background: var(--page-bg);
    font-family: "Open Sans", sans-serif;
  }
  .label {
    position: absolute;
    left: 146px;
    top: 60px;
    width: 866px;
    height: 1080px;
    background: var(--label-bg);
    overflow: hidden;
  }
  .leaf-art {
    position: absolute;
    left: 0;
    top: 60px;
    width: 760px;
    height: 820px;
    background: radial-gradient(ellipse 55% 50% at 60% 50%, rgba(118,184,58,0.22), rgba(168,212,106,0.10) 60%, rgba(255,255,255,0) 100%);
  }
  .brand {
    position: absolute;
    left: 282px;
    top: 398px;
    display: flex;
    align-items: flex-start;
    gap: 8px;
    color: var(--brand-green);
  }
  .brand-square {
    width: 40px;
    height: 40px;
    background: var(--brand-green);
    margin-top: 4px;
  }
  .brand-name {
    font-size: 36px;
    font-weight: 700;
    line-height: 38px;
    letter-spacing: 2px;
  }
  .brand-sub {
    font-size: 15px;
    font-weight: 700;
    line-height: 16px;
    letter-spacing: 0.5px;
  }
  .product-name {
    position: absolute;
    left: 130px;
    top: 456px;
    width: 510px;
    margin: 0;
    text-align: center;
    color: var(--brand-green);
    font-weight: 800;
    font-size: 122px;
    line-height: 116px;
    letter-spacing: -2px;
  }
  .blurb {
    position: absolute;
    left: 200px;
    top: 912px;
    width: 500px;
    margin: 0;
    font-size: 19px;
    line-height: 26px;
    color: var(--body-text);
  }
  .edge-tab {
    position: absolute;
    right: 0;
    top: 888px;
    width: 10px;
    height: 60px;
    background: var(--leaf-mid);
  }
</style>
</head>
<body>
  <main class="label">
    <div class="leaf-art" role="img" aria-label="Green leaf-swirl illustration of a stylised figure reaching toward a green sphere, with a flowing ribbon below"></div>

    <div class="brand">
      <div class="brand-square"></div>
      <div>
        <div class="brand-name">VERDAN</div>
        <div class="brand-sub">BIOTECH LIMITED</div>
      </div>
    </div>

    <h1 class="product-name">GOLD<br>PETAL<br>GRAIN</h1>

    <p class="blurb">Lorem ipsum dolor sit amet, consectetur adipisc-<br>ing elit. Ut mollis lobortis tempus. Donec lobortis</p>

    <div class="edge-tab"></div>
  </main>
</body>
</html>
```